wedding DJ & Lighting entertainment

We are a DJ and Lighting production company. We specialize mainly in wedding entertainment. I've attached my old postcard in the image folder, however, i would like something new and updated. You can use the same bullet points from the front page, but i would like to have a cleaner look on the front. I'd like to have one large image on the front side and smaller images on the back side. I'd also like to have some text below the logo. I'd like it to say DJ * Lighting * Audio/Visual. I'd also like to have the phrase "Celebrate with Style"

Target Market(s)

weddings, private events, women

Industry/Entity Type

It Company

Font styles to use
Sans Serif
Script

Requirements
Must have
• look elegant, sophisticated. Must have my new logo! My logo is attached as one of the files. It's a headphone logo.

```html
<!DOCTYPE html>
<html lang="en">
<head>
<meta charset="utf-8">
<title>Pulsenight Productions – Postcard</title>
<link rel="stylesheet" href="https://fonts.googleapis.com/css2?family=Open+Sans:ital,wght@0,400;0,600;0,700;0,800;1,700;1,800&family=Oswald:wght@500&family=Crimson+Text:ital,wght@1,600&display=swap">
<style>
  :root{
    --purple:#8a2a8f;
    --purple-deep:#6d1d73;
    --red:#e32424;
    --white:#ffffff;
    --stage:#8d8d8d;
  }
  *{box-sizing:border-box;margin:0;padding:0}
  html,body{width:1200px;height:900px;overflow:hidden}
  body{background:radial-gradient(ellipse at 50% 45%,#b8b8b8 0%,var(--stage) 60%,#5f5f5f 100%);font-family:"Open Sans",Arial,sans-serif;position:relative}

  .postcard{position:absolute;left:280px;width:640px;height:420px;overflow:hidden;box-shadow:0 8px 24px rgba(0,0,0,.35)}
  .postcard--front{top:22px;background:var(--purple)}
  .postcard--back{top:458px;background:var(--purple);padding:14px}

  /* FRONT */
  .front__topbar{position:absolute;left:0;top:0;width:100%;height:30px;display:flex;justify-content:space-between;align-items:center;padding:0 22px;color:var(--white);font-size:10px;font-weight:600;z-index:2}
  .front__logo-tab{position:absolute;left:210px;top:0;width:220px;height:50px;z-index:3}
  .front__logo-name{position:absolute;left:0;right:0;top:14px;text-align:center;font-weight:700;font-size:14px;color:var(--red);display:flex;justify-content:center;align-items:center;gap:6px}
  .front__logo-name .dot{width:9px;height:9px;border-radius:50%;background:var(--red)}
  .front__photo{position:absolute;left:0;right:6px;top:30px;height:268px;
    background:
      radial-gradient(ellipse 60px 40px at 32% 18%,rgba(255,190,240,.85),transparent 70%),
      radial-gradient(ellipse 60px 40px at 88% 16%,rgba(255,200,245,.8),transparent 70%),
      radial-gradient(ellipse 90px 30px at 62% 14%,rgba(230,140,220,.55),transparent 70%),
      radial-gradient(ellipse 160px 90px at 55% 62%,rgba(240,220,225,.55),transparent 70%),
      radial-gradient(ellipse 140px 80px at 82% 70%,rgba(120,150,190,.5),transparent 70%),
      radial-gradient(ellipse 180px 100px at 25% 78%,rgba(150,80,70,.6),transparent 70%),
      linear-gradient(180deg,#3a1f40 0%,#6b2f66 22%,#8a5a68 50%,#7a4a42 75%,#3d2424 100%)}
  .front__services{position:absolute;left:0;top:104px;display:flex;flex-direction:column;gap:6px;z-index:2;list-style:none}
  .front__service{font-family:"Oswald",Arial,sans-serif;font-weight:500;font-size:20px;letter-spacing:1.5px;color:#f3e6f4;background:rgba(176,78,180,.72);padding:1px 16px 1px 22px;width:max-content}
  .front__tagline-tab{position:absolute;left:196px;top:283px;width:248px;height:27px;background:var(--white);clip-path:polygon(6% 0,94% 0,100% 100%,0 100%);display:flex;justify-content:center;align-items:center;color:var(--red);font-weight:800;font-size:13px;z-index:2}
  .front__footer{position:absolute;left:0;right:0;top:312px;text-align:center;color:var(--white)}
  .front__book{font-weight:800;font-size:21px;letter-spacing:.3px;line-height:1.2}
  .front__company{font-weight:700;font-size:10.5px;margin-top:1px}
  .front__offers{font-weight:700;font-size:8.5px;margin-top:5px;letter-spacing:.3px}
  .front__offers--last{margin-top:14px}

  /* BACK */
  .back__frame{position:relative;width:100%;height:100%;background:var(--white);padding:4px}
  .back__collage{position:relative;width:100%;height:100%;overflow:hidden}
  .tile{position:absolute;border:2px solid var(--white)}
  .tile--dance-pink{left:0;top:0;width:360px;height:120px;background:
      radial-gradient(ellipse 120px 50px at 80% 10%,rgba(255,120,220,.9),transparent 70%),
      radial-gradient(ellipse 90px 40px at 30% 70%,rgba(90,170,170,.6),transparent 70%),
      radial-gradient(ellipse 100px 50px at 60% 80%,rgba(230,200,190,.55),transparent 70%),
      linear-gradient(160deg,#b43a96,#6b3a7a 55%,#3a2b4a)}
  .tile--ballroom{left:0;top:120px;width:250px;height:264px;background:
      radial-gradient(ellipse 70px 30px at 25% 20%,rgba(140,160,255,.8),transparent 70%),
      radial-gradient(ellipse 60px 30px at 80% 22%,rgba(240,180,90,.7),transparent 70%),
      radial-gradient(ellipse 110px 60px at 55% 70%,rgba(190,150,230,.7),transparent 70%),
      linear-gradient(180deg,#1e2a70,#3a4cb0 40%,#6a5cb8 70%,#2e2f66)}
  .tile--first-dance{left:360px;top:0;width:130px;height:58px;background:
      radial-gradient(ellipse 30px 20px at 70% 50%,rgba(235,235,240,.7),transparent 70%),
      linear-gradient(180deg,#2a1e33,#5a3a6a)}
  .tile--mono-crowd{left:360px;top:58px;width:130px;height:132px;background:
      radial-gradient(ellipse 60px 40px at 40% 40%,rgba(235,235,235,.8),transparent 70%),
      radial-gradient(ellipse 50px 30px at 75% 75%,rgba(190,190,190,.6),transparent 70%),
      linear-gradient(180deg,#2e2e2e,#8a8a8a 55%,#404040)}
  .tile--cheer{left:250px;top:120px;width:110px;height:70px;background:
      radial-gradient(ellipse 40px 25px at 50% 40%,rgba(220,220,220,.7),transparent 70%),
      linear-gradient(200deg,#3a3a3a,#8a8a8a 60%,#2a2a2a)}
  .tile--couple{left:250px;top:190px;width:240px;height:100px;background:
      radial-gradient(ellipse 50px 35px at 65% 60%,rgba(230,220,200,.6),transparent 70%),
      radial-gradient(ellipse 60px 30px at 30% 50%,rgba(180,60,60,.5),transparent 70%),
      linear-gradient(150deg,#173232,#2f5650 50%,#5a4a3a)}
  .tile--mono-party{left:250px;top:290px;width:240px;height:94px;background:
      radial-gradient(ellipse 70px 30px at 40% 50%,rgba(220,220,220,.7),transparent 70%),
      linear-gradient(200deg,#222,#7d7d7d 55%,#333)}
  .tile--tables{left:490px;top:0;width:114px;height:95px;background:
      radial-gradient(ellipse 30px 18px at 55% 40%,rgba(250,220,170,.7),transparent 70%),
      linear-gradient(180deg,#2e2260,#6a4ab0)}
  .tile--guests{left:490px;top:95px;width:114px;height:75px;background:
      radial-gradient(ellipse 40px 20px at 50% 60%,rgba(220,200,190,.6),transparent 70%),
      linear-gradient(180deg,#3e3030,#7a6a6a)}
  .tile--centerpiece{left:490px;top:170px;width:114px;height:214px;background:
      radial-gradient(ellipse 40px 30px at 55% 45%,rgba(250,220,200,.85),transparent 70%),
      linear-gradient(180deg,#5a4aa8,#8a74d0 50%,#3a2e80)}
  .back__banner{position:absolute;left:-30px;top:150px;width:700px;height:54px;transform:rotate(9deg);transform-origin:left center;z-index:2}
  .back__band{position:absolute;left:0;top:0;width:100%;height:100%;background:var(--red);border-top:3px solid var(--white);border-bottom:3px solid var(--white);display:flex;align-items:center;padding-left:42px;color:var(--white);font-weight:800;font-style:italic;font-size:30px;letter-spacing:.5px}
  .back__logo{position:absolute;left:476px;top:-14px;width:176px;height:80px;border-radius:50%;background:var(--white);display:flex;flex-direction:column;align-items:center;justify-content:center;gap:2px}
  .back__logo-name{font-weight:700;font-size:20px;color:var(--red);display:flex;align-items:center;gap:6px}
  .back__logo-name .dot{width:10px;height:10px;border-radius:50%;background:var(--red)}
  .back__logo-services{font-weight:700;font-size:8.5px;color:var(--red);letter-spacing:.4px}
  .back__caption{position:absolute;right:10px;bottom:6px;text-align:right;color:var(--white);font-family:"Crimson Text",Georgia,serif;font-style:italic;font-weight:600;font-size:17px;line-height:1.1;z-index:2;text-shadow:0 1px 3px rgba(0,0,0,.6)}
</style>
</head>
<body>

<section class="postcard postcard--front">
  <div class="front__photo" role="img" aria-label="Large photo of wedding guests dancing in a ballroom with purple uplighting"></div>
  <header class="front__topbar">
    <span class="front__web">www.pulsenightpros.com</span>
    <span class="front__email">hello@pulsenightpros.com</span>
  </header>
  <div class="front__logo-tab">
    <svg width="220" height="50" viewBox="0 0 220 50" aria-hidden="true">
      <path d="M0 0 C40 0 40 44 80 44 L140 44 C180 44 180 0 220 0 Z" fill="#ffffff"/>
    </svg>
    <div class="front__logo-name"><span class="dot"></span>Pulsenight</div>
  </div>
  <ul class="front__services">
    <li class="front__service">DJ</li>
    <li class="front__service">LIGHTING</li>
    <li class="front__service">AUDIO/VISUAL</li>
  </ul>
  <div class="front__tagline-tab">CELEBRATE WITH STYLE</div>
  <footer class="front__footer">
    <p class="front__book">BOOK NOW: 888-555-0142</p>
    <p class="front__company">Pulsenight Productions DJ &amp; Lighting Entertainment</p>
    <p class="front__offers">DJ &amp; EMCEE ENTERTAINMENT &nbsp;·&nbsp; CUSTOMIZED LIGHTING DECOR &nbsp;·&nbsp; EVENT HOSTING &amp; COORDINATION</p>
    <p class="front__offers front__offers--last">PERSONALIZED SERVICE &nbsp;·&nbsp; HELPFUL PLANNING TOOLS</p>
  </footer>
</section>

<section class="postcard postcard--back">
  <div class="back__frame">
    <div class="back__collage">
      <div class="tile tile--dance-pink" role="img" aria-label="Photo of guests dancing under pink lights"></div>
      <div class="tile tile--ballroom" role="img" aria-label="Photo of ballroom with blue uplighting and monogram projected on the dance floor"></div>
      <div class="tile tile--first-dance" role="img" aria-label="Photo of a couple's first dance in a dim hall"></div>
      <div class="tile tile--mono-crowd" role="img" aria-label="Black and white photo of a dancing crowd"></div>
      <div class="tile tile--cheer" role="img" aria-label="Black and white photo of guests cheering"></div>
      <div class="tile tile--couple" role="img" aria-label="Photo of a couple dancing at a reception"></div>
      <div class="tile tile--mono-party" role="img" aria-label="Black and white photo of guests celebrating"></div>
      <div class="tile tile--tables" role="img" aria-label="Photo of reception tables in purple light"></div>
      <div class="tile tile--guests" role="img" aria-label="Photo of seated guests"></div>
      <div class="tile tile--centerpiece" role="img" aria-label="Photo of a floral centerpiece lit in violet"></div>

      <div class="back__banner">
        <div class="back__band">CELEBRATE WITH STYLE</div>
        <div class="back__logo">
          <span class="back__logo-name"><span class="dot"></span>Pulsenight</span>
          <span class="back__logo-services">DJ • LIGHTING • AUDIO/VISUAL</span>
        </div>
      </div>

      <p class="back__caption">Creating memories...<br>one event at a time</p>
    </div>
  </div>
</section>

</body>
</html>
```